Suitor Prediction Show Graphic

I need a graphic for that looks like a fancy spread sheet for a predictions game for a reality show. I want there to be 3 columns, 1:Player A, 2: Question, 3: Player B. There should be at least 10 rows. I am looking for a photoshop template that I can customize later. I have attached the graphic needed for the name of the shows as well as a very basic version of what I am looking for. Please let me know if you need additional information. It should be themed with roses and wedding rings.
SIZE:
1080px by 1920px

Font styles to use
Decorative

Colors
ec1f27
9bcb3c

Requirements
Must have
• The logo for Quelvo and Tindrel. 1080px by 1920px in size.
Nice to have
• Would be nice to have rose vines as the dividers

```html
<!DOCTYPE html>
<html lang="en">
<head>
<meta charset="utf-8">
<title>Suitor Prediction Show Sheet</title>
<link rel="stylesheet" href="https://fonts.googleapis.com/css2?family=Playfair+Display:wght@400;700&family=Lora:wght@400;500&display=swap">
<style>
  :root{
    --cream:#f4e7c9;
    --cream-light:#fbf3e1;
    --gold:#d9b877;
    --pink-top:#f6c9da;
    --pink-soft:#fcebf1;
    --mauve:#b3436f;
    --mauve-dark:#8e2f57;
    --rose-red:#ec1f27;
    --leaf:#9bcb3c;
    --answer:#8a6b47;
    --navy:#1d2a5c;
  }
  *{box-sizing:border-box;margin:0;padding:0}
  html,body{width:675px;height:1200px;overflow:hidden;background:var(--cream)}
  .sheet{position:relative;width:675px;height:1200px;overflow:hidden;
    background:linear-gradient(var(--cream-light),var(--cream));font-family:"Lora",serif}

  .header{position:absolute;left:0;top:0;width:675px;height:190px;
    background:linear-gradient(180deg,var(--pink-top) 0%,var(--pink-soft) 70%,var(--cream-light) 100%)}
  .corner-art{position:absolute;top:8px;width:80px;height:80px;border-radius:12px;
    background:linear-gradient(160deg,#f3dcb0,#e9c7a0 55%,#f2c3d3)}
  .corner-art-left{left:6px}
  .corner-art-right{right:6px}
  .name-band{position:absolute;left:88px;top:20px;width:499px;height:32px;
    background:linear-gradient(90deg,var(--mauve-dark),var(--mauve) 20%,#d889a8 50%,var(--mauve) 80%,var(--mauve-dark));
    display:flex;justify-content:space-between;align-items:center;padding:0 26px}
  .player-name{font-family:"Playfair Display",serif;color:#fff;font-size:22px;letter-spacing:1px}
  .show-name{position:absolute;left:0;width:675px;top:10px;text-align:center;
    font-family:"Playfair Display",serif;font-weight:700;font-size:36px;color:var(--rose-red);line-height:52px}
  .show-name span{background:var(--pink-soft);padding:0 10px;border-radius:8px}
  .garland{position:absolute;top:100px;width:265px;height:44px;border-radius:22px;
    background:linear-gradient(90deg,#e99bb7,#f5c4d5 40%,#a9c98a 60%,#e99bb7)}
  .garland-left{left:8px}
  .garland-right{right:8px}
  .challenge{position:absolute;left:297px;top:94px;width:81px;display:flex;flex-direction:column;align-items:center;gap:4px}
  .challenge-mark{width:34px;height:34px;background:var(--navy)}
  .challenge-name{font-family:"Playfair Display",serif;font-size:18px;color:var(--navy);line-height:1}

  .rows{position:absolute;left:0;top:187px;width:675px}
  .row{position:relative;width:675px;height:101px}
  .row svg.band{position:absolute;left:0;top:0;width:675px;height:101px}
  .answer{position:absolute;top:34px;width:200px;text-align:center;font-size:24px;line-height:30px;color:var(--answer)}
  .answer-a{left:6px}
  .answer-b{right:6px}
  .question{position:absolute;left:262px;top:20px;width:151px;text-align:center;color:var(--rose-red);
    font-family:"Playfair Display",serif}
  .question .num{font-size:21px;font-weight:700;line-height:1}
  .question .num sup{font-size:10px}
  .question .label{font-size:11px;line-height:1.2}
  .roses{position:absolute;left:254px;top:70px;width:167px;height:24px;border-radius:12px;
    background:linear-gradient(90deg,#a9c98a,#ee9fbb 30%,#f7c7d7 50%,#ee9fbb 70%,#a9c98a)}
</style>
</head>
<body>
<main class="sheet">
  <header class="header">
    <div class="corner-art corner-art-left" role="img" aria-label="Wedding ring with roses illustration"></div>
    <div class="corner-art corner-art-right" role="img" aria-label="Wedding ring with roses illustration"></div>
    <div class="name-band">
      <span class="player-name">TIM</span>
      <span class="player-name">AB</span>
    </div>
    <div class="show-name"><span>Tindrel</span></div>
    <div class="garland garland-left" role="img" aria-label="Pink rose vine garland"></div>
    <div class="garland garland-right" role="img" aria-label="Pink rose vine garland"></div>
    <div class="challenge">
      <div class="challenge-mark"></div>
      <div class="challenge-name">Quelvo</div>
    </div>
  </header>

  <section class="rows">
    <svg width="0" height="0" style="position:absolute">
      <defs>
        <symbol id="band" viewBox="0 0 675 101">
          <path d="M0,10 C180,-3 300,32 470,21 C560,14 620,5 675,11 L675,101 L0,101 Z" fill="#f6eacd"/>
          <path d="M0,10 C180,-3 300,32 470,21 C560,14 620,5 675,11" fill="none" stroke="#d9b877" stroke-width="2"/>
          <path d="M0,15 C180,2 300,37 470,26 C560,19 620,10 675,16" fill="none" stroke="#efdcb0" stroke-width="3"/>
          <path d="M262,84 A75.5,68 0 0 1 413,84 Z" fill="#fdf7ea" stroke="#d9b877" stroke-width="1.5"/>
        </symbol>
      </defs>
    </svg>

    <div class="row"><svg class="band"><use href="#band"/></svg><div class="answer answer-a">Answer 1</div><div class="question"><div class="num">1<sup>st</sup></div><div class="label">Question</div></div><div class="roses" role="img" aria-label="Rose vine divider"></div><div class="answer answer-b">Answer 2</div></div>
    <div class="row"><svg class="band"><use href="#band"/></svg><div class="answer answer-a">Answer 1</div><div class="question"><div class="num">1<sup>st</sup></div><div class="label">Question</div></div><div class="roses" role="img" aria-label="Rose vine divider"></div><div class="answer answer-b">Answer 2</div></div>
    <div class="row"><svg class="band"><use href="#band"/></svg><div class="answer answer-a">Answer 1</div><div class="question"><div class="num">1<sup>st</sup></div><div class="label">Question</div></div><div class="roses" role="img" aria-label="Rose vine divider"></div><div class="answer answer-b">Answer 2</div></div>
    <div class="row"><svg class="band"><use href="#band"/></svg><div class="answer answer-a">Answer 1</div><div class="question"><div class="num">1<sup>st</sup></div><div class="label">Question</div></div><div class="roses" role="img" aria-label="Rose vine divider"></div><div class="answer answer-b">Answer 2</div></div>
    <div class="row"><svg class="band"><use href="#band"/></svg><div class="answer answer-a">Answer 1</div><div class="question"><div class="num">1<sup>st</sup></div><div class="label">Question</div></div><div class="roses" role="img" aria-label="Rose vine divider"></div><div class="answer answer-b">Answer 2</div></div>
    <div class="row"><svg class="band"><use href="#band"/></svg><div class="answer answer-a">Answer 1</div><div class="question"><div class="num">1<sup>st</sup></div><div class="label">Question</div></div><div class="roses" role="img" aria-label="Rose vine divider"></div><div class="answer answer-b">Answer 2</div></div>
    <div class="row"><svg class="band"><use href="#band"/></svg><div class="answer answer-a">Answer 1</div><div class="question"><div class="num">1<sup>st</sup></div><div class="label">Question</div></div><div class="roses" role="img" aria-label="Rose vine divider"></div><div class="answer answer-b">Answer 2</div></div>
    <div class="row"><svg class="band"><use href="#band"/></svg><div class="answer answer-a">Answer 1</div><div class="question"><div class="num">1<sup>st</sup></div><div class="label">Question</div></div><div class="roses" role="img" aria-label="Rose vine divider"></div><div class="answer answer-b">Answer 2</div></div>
    <div class="row"><svg class="band"><use href="#band"/></svg><div class="answer answer-a">Answer 1</div><div class="question"><div class="num">1<sup>st</sup></div><div class="label">Question</div></div><div class="roses" role="img" aria-label="Rose vine divider"></div><div class="answer answer-b">Answer 2</div></div>
    <div class="row"><svg class="band"><use href="#band"/></svg><div class="answer answer-a">Answer 1</div><div class="question"><div class="num">1<sup>st</sup></div><div class="label">Question</div></div><div class="roses" role="img" aria-label="Rose vine divider"></div><div class="answer answer-b">Answer 2</div></div>
  </section>
</main>
</body>
</html>
```